Flyer with pull tabs

This project is to redo/update my pull tab flier
The Top line should be Need Health Insurance?
Please add as many images as in the design as possible.
The size should be 8.5 X 11 size
The information needs to be with Bluefield Insurance Services LLC information.
You will use the phone number (555) 318-2097 and the email address Odessa@CoveragePalPro.com
The slogan is “Simplifying the Benefits Solution Process”
Life | Health | Retirement | Long-Term Care

```html
<!DOCTYPE html>
<html lang="en">
<head>
<meta charset="utf-8">
<title>Need Health Insurance? – Pull Tab Flyer</title>
<link href="https://fonts.googleapis.com/css2?family=Montserrat:wght@400;500;600;700;800&display=swap" rel="stylesheet">
<style>
:root{
  --bg:#9d9d9d;
  --paper:#ffffff;
  --teal:#20c2b4;
  --purple:#6a4c9c;
  --ink:#2a2a2a;
  --blue:#1d3f9a;
  --green:#1f8a45;
  --crimson:#b8174a;
  --orange:#dd4a1c;
  --dot:#20c2b4;
}
*{box-sizing:border-box;margin:0;padding:0}
html,body{width:1200px;height:1200px;overflow:hidden;background:var(--bg);font-family:"Montserrat",sans-serif}
.flyer{position:absolute;left:175px;top:50px;width:850px;height:1100px;background:var(--paper);box-shadow:0 6px 24px rgba(0,0,0,.25)}
.headline-band{position:absolute;left:40px;top:40px;width:700px;height:84px}
.headline-band .shadow{position:absolute;left:12px;top:12px;right:-12px;bottom:-12px;background:var(--purple)}
.headline-band .face{position:absolute;inset:0;background:var(--teal);display:flex;align-items:center;justify-content:center}
.headline{color:var(--purple);font-weight:800;font-size:41px;letter-spacing:1.5px;white-space:nowrap}
.subhead{position:absolute;left:0;right:0;top:150px;text-align:center;font-weight:700;font-size:25px;color:var(--purple);letter-spacing:1.5px;white-space:nowrap}
.collage{position:absolute;left:40px;top:196px;width:770px;height:300px}
.photo{position:absolute}
.p1{left:0;top:0;width:250px;height:140px;background:linear-gradient(135deg,#d9c6b4,#8c7462)}
.p2{left:0;top:148px;width:250px;height:152px;background:linear-gradient(135deg,#c7d6dc,#8a9aa3)}
.p3{left:258px;top:0;width:250px;height:300px;background:linear-gradient(160deg,#ece8e2,#a59a8e)}
.p4{left:516px;top:0;width:254px;height:150px;background:linear-gradient(135deg,#6f5a4d,#c9a796)}
.p5{left:516px;top:158px;width:254px;height:142px;background:linear-gradient(135deg,#f1dcc8,#c99d7d)}
.helping{position:absolute;left:0;right:0;top:516px;text-align:center;font-weight:700;font-size:20px;color:var(--purple);letter-spacing:.8px;white-space:nowrap}
.coverage{position:absolute;left:0;right:0;top:552px;text-align:center;font-weight:500;font-size:21px;color:var(--ink);letter-spacing:1px;white-space:nowrap}
.coverage .dot{color:var(--dot);margin:0 12px}
.contact-line{position:absolute;left:0;right:0;top:596px;text-align:center;font-weight:600;font-size:18px;color:var(--purple);white-space:nowrap}
.agent{position:absolute;left:40px;top:640px;width:420px;height:200px}
.agent-photo{position:absolute;left:0;top:0;width:150px;height:165px;border:5px solid var(--purple);background:linear-gradient(160deg,#5a3b2c,#1e1512)}
.agent-name{position:absolute;left:170px;top:8px;font-weight:700;font-size:24px;color:var(--purple);white-space:nowrap}
.agent-title{position:absolute;left:170px;top:42px;font-size:14px;color:var(--ink);white-space:nowrap}
.agent-phone{position:absolute;left:170px;top:66px;font-weight:700;font-size:29px;color:var(--purple);white-space:nowrap}
.agent-email{position:absolute;left:170px;top:108px;font-size:14px;color:var(--ink);white-space:nowrap}
.agency-id{position:absolute;left:40px;top:176px;font-size:14px;color:var(--ink);white-space:nowrap}
.brand{position:absolute;left:470px;top:640px;width:350px;height:200px}
.slogan{position:absolute;left:0;top:4px;font-weight:700;font-size:15px;color:var(--purple);line-height:1.3;white-space:nowrap}
.brand-name{position:absolute;left:0;top:70px;display:flex;align-items:center;gap:10px;font-weight:700;font-size:17px;color:var(--teal);white-space:nowrap}
.brand-name .mark{width:26px;height:26px;border-radius:50%;background:var(--teal);flex:none}
.lines{position:absolute;left:0;top:124px;font-size:12.5px;color:var(--purple);letter-spacing:.3px;white-space:nowrap}
.bars{position:absolute;left:0;right:0;top:868px;height:12px;display:flex}
.bars span{flex:1}
.bars span:nth-child(1){background:var(--blue)}
.bars span:nth-child(2){background:var(--green)}
.bars span:nth-child(3){background:var(--crimson)}
.bars span:nth-child(4){background:var(--orange)}
.tabs{position:absolute;left:0;right:0;top:880px;bottom:0;display:flex}
.tab{flex:1;border-right:1px dashed #555;display:flex;justify-content:center;padding-top:14px}
.tab:last-child{border-right:none}
.tab-text{writing-mode:vertical-rl;font-size:11px;line-height:1.25;color:var(--ink);white-space:nowrap}
.tab-text strong{font-weight:700}
</style>
</head>
<body>
<main class="flyer">
  <div class="headline-band"><div class="shadow"></div><div class="face"><h1 class="headline">NEED HEALTH INSURANCE?</h1></div></div>
  <p class="subhead">AFFORDABLE SOLUTIONS CENTERED AROUND YOU</p>

  <section class="collage">
    <div class="photo p1" role="img" aria-label="Photo of a mother smiling with her daughters"></div>
    <div class="photo p2" role="img" aria-label="Photo of a father and children playing on the floor at home"></div>
    <div class="photo p3" role="img" aria-label="Photo of a family in a bright kitchen"></div>
    <div class="photo p4" role="img" aria-label="Photo of parents kissing their baby"></div>
    <div class="photo p5" role="img" aria-label="Photo of a laughing couple"></div>
  </section>

  <p class="helping">HELPING OUR LOCAL SMALL BUSINESSES, FAMILIES AND INDIVIDUALS</p>
  <p class="coverage">HEALTH<span class="dot">•</span>DENTAL<span class="dot">•</span>VISION<span class="dot">•</span>DISABILITY<span class="dot">•</span>AND MORE!</p>
  <p class="contact-line">For personalized service in your area, contact your local Bluefield agent today</p>

  <section class="agent">
    <div class="agent-photo" role="img" aria-label="Portrait photo of the insurance agent"></div>
    <h2 class="agent-name">Odessa Marlow</h2>
    <p class="agent-title">Licensed Insurance Agent</p>
    <p class="agent-phone">(555) 318-2097</p>
    <p class="agent-email">Odessa@CoveragePalPro.com</p>
    <p class="agency-id">Bluefield Insurance Services llc. 4826013</p>
  </section>

  <section class="brand">
    <p class="slogan">SIMPLIFYING THE BENEFITS<br>SOLUTION PROCESS</p>
    <div class="brand-name"><span class="mark"></span>Bluefield Insurance Services LLC</div>
    <p class="lines">LIFE | HEALTH | RETIREMENT | LONG-TERM CARE</p>
  </section>

  <div class="bars"><span></span><span></span><span></span><span></span></div>
  <div class="tabs">
    <div class="tab"><p class="tab-text"><strong>INSURANCE SOLUTIONS</strong><br><strong>(555) 318-2097</strong><br>ODESSA@COVERAGEPALPRO.COM</p></div>
    <div class="tab"><p class="tab-text"><strong>INSURANCE SOLUTIONS</strong><br><strong>(555) 318-2097</strong><br>ODESSA@COVERAGEPALPRO.COM</p></div>
    <div class="tab"><p class="tab-text"><strong>INSURANCE SOLUTIONS</strong><br><strong>(555) 318-2097</strong><br>ODESSA@COVERAGEPALPRO.COM</p></div>
    <div class="tab"><p class="tab-text"><strong>INSURANCE SOLUTIONS</strong><br><strong>(555) 318-2097</strong><br>ODESSA@COVERAGEPALPRO.COM</p></div>
    <div class="tab"><p class="tab-text"><strong>INSURANCE SOLUTIONS</strong><br><strong>(555) 318-2097</strong><br>ODESSA@COVERAGEPALPRO.COM</p></div>
    <div class="tab"><p class="tab-text"><strong>INSURANCE SOLUTIONS</strong><br><strong>(555) 318-2097</strong><br>ODESSA@COVERAGEPALPRO.COM</p></div>
    <div class="tab"><p class="tab-text"><strong>INSURANCE SOLUTIONS</strong><br><strong>(555) 318-2097</strong><br>ODESSA@COVERAGEPALPRO.COM</p></div>
    <div class="tab"><p class="tab-text"><strong>INSURANCE SOLUTIONS</strong><br><strong>(555) 318-2097</strong><br>ODESSA@COVERAGEPALPRO.COM</p></div>
  </div>
</main>
</body>
</html>
```